Optometrist/Eye Care Clinic Business card with new logo attached

We are a small, independent eye care clinic in Canada. We have recently updated our logo (as attached), and would like a professional, modern and health care oriented business card to highlight our office details and our optometrist. We'd like to incorporate the blue colours as seen on our logo.

Target Market(s)

demographic: age 35-65 male/female equal

Industry/Entity Type

Health Care

Contact Information for Business Card

Name of clinic: "Marrow Bend Eye Care Optometry"

Font styles to use
Sans Serif

Colors
0355a3

Requirements
Must have
• our website: marrowbendeyecare.com
• Dr Lena Quorvik
• Optometrist
• 217-392 E Halvering Ave
• Vancouver BC V6R 3J8
• P: 604-319-2058
• E: info@marrowbendeyecare.com
Nice to have
• front side: logo/name of clinic as seen on logo attached and website
• backside: logo on the left side, and name/title/address/phone/email

```html
<!DOCTYPE html>
<html lang="en">
<head>
<meta charset="utf-8">
<title>Marrow Bend Eye Care Optometry – Business Card</title>
<link rel="stylesheet" href="https://fonts.googleapis.com/css2?family=Arimo:wght@400;600&display=swap">
<style>
  :root {
    --backdrop: #b9b9b9;
    --card-white: #f6f6f6;
    --brand-deep: #0e4d6a;
    --panel-top: #1c7ea4;
    --panel-bottom: #0d4560;
    --text-grey: #4a4a4a;
    --text-on-blue: #ffffff;
  }
  * { box-sizing: border-box; margin: 0; padding: 0; }
  html, body { width: 1200px; height: 960px; overflow: hidden; }
  body {
    background: var(--backdrop);
    font-family: "Arimo", Arial, sans-serif;
    position: relative;
  }
  .card {
    position: absolute;
    width: 600px;
    height: 342px;
    border-radius: 18px;
    background: var(--card-white);
    overflow: hidden;
  }
  .card--front { left: 322px; top: 108px; }
  .card--back { left: 320px; top: 493px; }

  /* Front */
  .brand-mark {
    position: absolute;
    left: 0; right: 0; top: 84px;
    display: flex; flex-direction: column; align-items: center;
    color: var(--brand-deep);
  }
  .brand-mark__dot {
    width: 70px; height: 70px; border-radius: 50%;
    background: var(--brand-deep);
    margin-bottom: 20px;
  }
  .brand-mark__name {
    text-align: center;
    text-transform: uppercase;
    letter-spacing: 3px;
    font-size: 19px;
    line-height: 1.35;
  }
  .front-web {
    position: absolute;
    left: 0; right: 0; top: 302px;
    text-align: center;
    font-size: 14px;
    letter-spacing: 2.6px;
    color: var(--text-grey);
  }

  /* Back */
  .back-panel { position: absolute; inset: 0; }
  .back-brand {
    position: absolute;
    left: 40px; top: 60px; width: 200px;
    display: flex; flex-direction: column; align-items: center;
    color: var(--brand-deep);
  }
  .back-brand__dot {
    width: 110px; height: 110px; border-radius: 50%;
    background: var(--brand-deep);
    margin-bottom: 16px;
  }
  .back-brand__name {
    text-align: center;
    text-transform: uppercase;
    font-size: 12px;
    letter-spacing: 1.6px;
    line-height: 1.4;
  }
  .contact {
    position: absolute;
    right: 36px;
    text-align: right;
    color: var(--text-on-blue);
  }
  .contact--person { top: 50px; }
  .contact__name { font-size: 22px; font-weight: 600; line-height: 1.2; }
  .contact__title { font-size: 15px; line-height: 1.2; }
  .contact--details { top: 200px; font-size: 14px; line-height: 19px; }
  .contact__block + .contact__block { margin-top: 9px; }
</style>
</head>
<body>
  <section class="card card--front" aria-label="Card front">
    <div class="brand-mark">
      <span class="brand-mark__dot"></span>
      <p class="brand-mark__name">Marrow Bend<br>Eye Care<br>Optometry</p>
    </div>
    <p class="front-web">www.marrowbendeyecare.com</p>
  </section>

  <section class="card card--back" aria-label="Card back">
    <svg class="back-panel" width="600" height="342" viewBox="0 0 600 342" aria-hidden="true">
      <defs>
        <linearGradient id="panelBlue" x1="0" y1="0" x2="0.4" y2="1">
          <stop offset="0" stop-color="#1c7ea4"/>
          <stop offset="1" stop-color="#0d4560"/>
        </linearGradient>
      </defs>
      <path d="M312,0 C326,120 314,250 250,342 L600,342 L600,0 Z" fill="url(#panelBlue)"/>
    </svg>

    <div class="back-brand">
      <span class="back-brand__dot"></span>
      <p class="back-brand__name">Marrow Bend<br>Eye Care Optometry</p>
    </div>

    <div class="contact contact--person">
      <p class="contact__name">Dr Lena Quorvik</p>
      <p class="contact__title">Optometrist</p>
    </div>

    <div class="contact contact--details">
      <div class="contact__block">
        <p>217-392 E Halvering Ave</p>
        <p>Vancouver BC V6R 3J8</p>
      </div>
      <div class="contact__block">
        <p>604-319-2058</p>
        <p>info@marrowbendeyecare.com</p>
        <p>marrowbendeyecare.com</p>
      </div>
    </div>
  </section>
</body>
</html>
```